Graphics for Blog Post Series

We are looking for 3 infographic style designs (see attached examples) to be used in a blog post series about CDL training. This blog post series includes 3 separate posts (links provided below) and the graphics should have a consistent look and feel across all 3 posts.

The point of each graphic is to have a visual representation of content discussed in each post and tell the story of that post. It should be something that will allow people to get an idea of what the post is about by looking at a visual.

The 3 mini graphics can be used independently with each post or all as one larger image that flows together (as shown in the attached example)

The size of each individual image should be 802 X 372. The size of all images put together (stacked on top of each other) should be 802 X 1117

Blog Post #1: http://brightroutelessons.example/blog/top-10-reasons-to-choose-company-sponsored-cdl-training/

Ideas for graphic: some type of graphic to represent a Top 10 List with a couple numbers and examples from the post. Text can be used to make the purpose of the image clear (as shown in example)

Blog Post #2: http://brightroutelessons.example/blog/pay-for-cdl-training/

Ideas for graphic: graphic showing money being held up (possibly by a person's hand) and words "How to pay for CDL training"

Blog Post #3: http://brightroutelessons.example/blog/cdl-job-opportunity/

Ideas for graphic: show a truck (similar to one in pitfall example) with a flat tire and indicate visually that a CDL with no job isn't going anywhere.

Again, we want these graphics to be very similar to the examples attached as they will be used in the same manner.

```html
<!DOCTYPE html>
<html lang="en">
<head>
<meta charset="utf-8">
<title>CDL Training Blog Series Graphics</title>
<link rel="stylesheet" href="https://fonts.googleapis.com/css2?family=Montserrat:wght@800;900&display=swap">
<style>
  :root {
    --yellow: #fbcb6b;
    --green-dark: #43943a;
    --green-light: #5bbb46;
    --white: #ffffff;
    --page: #ffffff;
  }
  * { box-sizing: border-box; margin: 0; padding: 0; }
  html, body { width: 1200px; height: 1000px; overflow: hidden; background: var(--page); }
  body { position: relative; font-family: "Montserrat", Arial, sans-serif; font-weight: 900; text-transform: uppercase; }
  .panel { position: absolute; left: 293px; width: 665px; height: 306px; background: var(--yellow); overflow: hidden; }
  .panel--reasons { top: 22px; }
  .panel--pay { top: 337px; height: 308px; }
  .panel--flat-tire { top: 653px; height: 305px; }
  .abs { position: absolute; }

  /* Panel 1 */
  .reasons-title { left: 372px; top: 0; width: 293px; height: 130px; background: var(--green-light); padding: 40px 0 0 10px; }
  .reasons-title__main { color: var(--yellow); font-size: 27px; line-height: 1; letter-spacing: .3px; white-space: nowrap; }
  .reasons-title__sub { color: var(--white); font-size: 15px; line-height: 20px; margin-top: 6px; font-weight: 800; white-space: nowrap; }
  .cell { position: absolute; width: 86px; height: 86px; color: var(--white); font-size: 56px; display: flex; align-items: center; justify-content: center; }
  .cell--dark { background: var(--green-dark); }
  .cell--light { background: var(--green-light); }
  .cell__tag { position: absolute; left: 7px; top: 3px; font-size: 16px; line-height: 1; }
  .cell__money { font-size: 30px; letter-spacing: -2px; margin-top: 10px; }
  .cell__art { position: absolute; border-radius: 4px; background: linear-gradient(#ffffff, #dfeedd); }
  .reason-label { color: var(--green-dark); font-size: 14.5px; line-height: 19px; font-weight: 800; white-space: nowrap; }
  .reason-label--job { right: 494px; top: 72px; text-align: right; }
  .reason-label--tuition { left: 378px; top: 150px; font-size: 18px; line-height: 23px; }
  .reason-label--instructors { left: 465px; top: 236px; }

  /* Panel 2 */
  .pay-band { left: 0; top: 175px; width: 665px; height: 133px; background: var(--green-dark); }
  .pay-art { left: 200px; top: 30px; width: 280px; height: 278px; background: linear-gradient(160deg, #ffffff 0%, #ffffff 40%, var(--green-light) 100%); }
  .pay-title { right: 475px; top: 38px; color: var(--green-dark); font-size: 45px; line-height: 50px; text-align: right; white-space: nowrap; }
  .pay-sub { left: 492px; top: 196px; color: var(--yellow); font-size: 28px; line-height: 34px; white-space: nowrap; }

  /* Panel 3 */
  .slogan { left: 0; top: 44px; width: 347px; height: 155px; background: var(--green-dark); padding: 12px 0 0 24px; font-size: 26px; line-height: 34px; white-space: nowrap; }
  .slogan__lead { color: var(--white); display: block; }
  .slogan__tail { color: var(--yellow); display: block; }
  .truck-art { left: 0; top: 75px; width: 519px; height: 190px; border-radius: 0 30px 20px 0; background: linear-gradient(180deg, #ffffff 0%, #ffffff 55%, var(--green-light) 75%, #ffffff 100%); }
  .road { left: 0; top: 0; }
</style>
</head>
<body>

<section class="panel panel--reasons" aria-label="Top 10 reasons to choose company sponsored CDL training">
  <div class="abs reasons-title">
    <div class="reasons-title__main">Top 10 Reasons</div>
    <div class="reasons-title__sub">To choose company<br>sponsored CDL training</div>
  </div>

  <p class="abs reason-label reason-label--job">Job opportunity<br>before training</p>
  <p class="abs reason-label reason-label--tuition">No upfront<br>tuition costs</p>
  <p class="abs reason-label reason-label--instructors">Learn from<br>instructors with<br>proven experience</p>

  <div class="cell cell--dark" style="left:191px;top:44px;"><span class="cell__tag" style="left:66px;">1</span><div class="cell__art" style="left:12px;top:16px;width:56px;height:64px;" role="img" aria-label="Bus with a driver's licence card"></div></div>
  <div class="cell cell--light" style="left:276px;top:44px;">2</div>

  <div class="cell cell--dark" style="left:105px;top:130px;">3</div>
  <div class="cell cell--light" style="left:191px;top:130px;">4</div>
  <div class="cell cell--dark" style="left:276px;top:130px;"><span class="cell__tag">5</span><span class="cell__money">$$$</span></div>

  <div class="cell cell--dark" style="left:20px;top:218px;">6</div>
  <div class="cell cell--light" style="left:105px;top:218px;">7</div>
  <div class="cell cell--dark" style="left:191px;top:218px;">8</div>
  <div class="cell cell--light" style="left:276px;top:218px;">9</div>
  <div class="cell cell--dark" style="left:361px;top:218px;"><span class="cell__tag">10</span><div class="cell__art" style="left:28px;top:10px;width:50px;height:72px;" role="img" aria-label="Instructor in cap with arms crossed"></div></div>
</section>

<section class="panel panel--pay" aria-label="How to pay for CDL training">
  <div class="abs pay-band"></div>
  <div class="abs pay-art" role="img" aria-label="Question mark surrounded by payment option icons"></div>
  <h2 class="abs pay-title">How<br>to pay</h2>
  <p class="abs pay-sub">For CDL<br>training</p>
</section>

<section class="panel panel--flat-tire" aria-label="CDL training without a job is like a truck with a flat tire">
  <svg class="abs road" width="665" height="305" viewBox="0 0 665 305" aria-hidden="true">
    <polygon points="0,265 540,265 665,300 665,305 0,305" fill="var(--green-dark)"/>
    <line x1="0" y1="290" x2="610" y2="290" stroke="var(--white)" stroke-width="3" stroke-dasharray="10 8"/>
    <rect x="604" y="120" width="4" height="165" fill="var(--green-dark)"/>
    <circle cx="606" cy="120" r="48" fill="var(--green-dark)"/>
    <circle cx="606" cy="120" r="40" fill="var(--green-light)"/>
    <rect x="582" y="113" width="48" height="14" fill="var(--white)"/>
  </svg>
  <div class="abs truck-art" role="img" aria-label="Flat-bed truck with a flat front tire"></div>
  <div class="abs slogan">
    <span class="slogan__lead">CDL training<br>without a job</span>
    <span class="slogan__tail">is like a truck<br>with a flat tire</span>
  </div>
</section>

</body>
</html>
```